Re-design of Business Card

We require a design for our business card.

Quorin is a supplier of industrial packaging specializing in plastic products. We are undergoing a rebranding to appear more corporate. We have changed our company name to quorin and have a new logo.

I have uploaded our old card design with the previous company name.
Don't copy the current design. We are looking for a new design.

Industry/Entity Type

Manufacturing

Contact Information for Business Card

please don't copy the current design. we are looking for a new design.

Font styles to use
Sans Serif

Colors

Designer to choose colors to be used in the design.

Requirements
Must have
• clean and easy to read.

```html
<!DOCTYPE html>
<html lang="en">
<head>
<meta charset="utf-8">
<title>Quorin Business Card</title>
<link rel="stylesheet" href="https://fonts.googleapis.com/css2?family=Libre+Baskerville:wght@400;700&family=Source+Sans+3:ital,wght@0,400;0,600;0,700;1,400&family=Roboto+Condensed:ital,wght@1,300&display=swap">
<style>
  :root {
    --orange: #ee7a0c;
    --charcoal: #545454;
    --slate: #878787;
    --map-grey: #666666;
    --tag-tan: #b9875a;
    --tag-text: #4b4b4b;
    --name-grey: #555555;
    --white: #ffffff;
    --edge: #8a8a8a;
  }
  * { box-sizing: border-box; margin: 0; padding: 0; }
  html, body { width: 1000px; height: 1200px; overflow: hidden; background: var(--white); }
  body { position: relative; font-family: "Source Sans 3", sans-serif; }

  .card { position: absolute; left: 165px; width: 663px; height: 427px; overflow: hidden; }
  .card-front { top: 126px; background: var(--white); border: 1px solid var(--edge); }
  .card-back { top: 644px; height: 429px; background: var(--charcoal); }

  .front-waves { position: absolute; left: 0; top: 0; width: 663px; height: 427px; }

  .brand-name {
    position: absolute; left: 366px; top: 34px;
    font-family: "Source Sans 3", sans-serif; font-weight: 700;
    font-size: 74px; letter-spacing: 3px; line-height: 1; color: var(--orange);
  }
  .person-name {
    position: absolute; left: 15px; top: 126px;
    font-family: "Libre Baskerville", serif; font-size: 24px; letter-spacing: 1px;
    color: var(--name-grey);
  }
  .person-role {
    position: absolute; left: 18px; top: 161px;
    font-family: "Source Sans 3", sans-serif; font-style: italic; font-size: 14.5px;
    letter-spacing: 0.5px; color: var(--orange);
  }

  .office-heading {
    position: absolute; left: 47px; top: 307px;
    font-family: "Libre Baskerville", serif; font-weight: 700; font-size: 17.5px;
    letter-spacing: 1.5px; color: var(--orange);
  }
  .office-lines { position: absolute; left: 47px; top: 331px; list-style: none; color: var(--white); font-size: 12.5px; }
  .office-lines li { height: 19.5px; line-height: 19.5px; }

  .contact-icon { position: absolute; width: 15px; height: 15px; }

  .direct-lines { position: absolute; right: 44px; top: 361px; list-style: none; text-align: right; color: var(--white); font-size: 13px; }
  .direct-lines li { height: 27px; line-height: 20px; }

  .range-group { position: absolute; left: 15px; color: var(--white); }
  .range-heading {
    font-family: "Libre Baskerville", serif; font-weight: 700; font-size: 17px;
    letter-spacing: 1.6px; color: var(--orange); line-height: 24px; margin-bottom: 1px;
  }
  .range-list { list-style: none; font-size: 16.5px; line-height: 21.6px; }

  .claim-tag {
    position: absolute; right: 0; height: 26px; padding: 0 9px 0 10px;
    background: var(--tag-tan); border-radius: 3px 0 0 3px;
    font-family: "Roboto Condensed", sans-serif; font-style: italic; font-weight: 300;
    font-size: 21px; line-height: 26px; color: var(--tag-text); white-space: nowrap;
  }

  .coverage-map {
    position: absolute; left: 220px; top: 86px; width: 430px; height: 280px;
    background: var(--map-grey);
    border-radius: 46% 40% 38% 48% / 42% 38% 52% 46%;
  }
  .site-marker {
    position: absolute; font-family: "Source Sans 3", sans-serif; font-weight: 700;
    font-size: 14px; color: var(--orange); letter-spacing: 0.5px; line-height: 1;
  }
</style>
</head>
<body>

<section class="card card-front" aria-label="Business card front">
  <svg class="front-waves" viewBox="0 0 663 427" aria-hidden="true">
    <path d="M448,264 C540,250 610,235 663,211 L663,318 C600,312 520,300 448,264 Z" fill="var(--orange)"/>
    <path d="M0,196 C150,178 330,196 450,262 C540,306 610,318 663,314 L663,318 C560,322 470,300 380,268 C280,240 150,250 0,272 Z" fill="var(--slate)"/>
    <path d="M0,272 C150,250 280,240 380,268 C470,300 560,322 663,316 L663,427 L0,427 Z" fill="var(--charcoal)"/>
    <path d="M0,272 C150,250 280,240 380,268 C470,300 560,322 663,316" fill="none" stroke="var(--white)" stroke-width="3"/>
  </svg>

  <div class="brand-name">QUORIN</div>
  <h1 class="person-name">Declan Marsh</h1>
  <p class="person-role">Machinery Sales Manager</p>

  <h2 class="office-heading">Head Office</h2>
  <svg class="contact-icon" style="left:27px;top:333px" viewBox="0 0 16 16" aria-hidden="true">
    <path d="M8,1 C4.8,1 2.5,3.4 2.5,6.3 C2.5,10 8,15 8,15 C8,15 13.5,10 13.5,6.3 C13.5,3.4 11.2,1 8,1 Z" fill="var(--orange)"/>
    <circle cx="8" cy="6.3" r="2.2" fill="var(--charcoal)"/>
  </svg>
  <svg class="contact-icon" style="left:26px;top:362px;width:17px;height:17px" viewBox="0 0 16 16" aria-hidden="true">
    <path d="M3,2 L5.5,2 L6.5,5 L5,6.3 C5.8,8 7.8,10 9.7,10.9 L11,9.4 L14,10.4 L14,13 C9,14 2,7 3,2 Z" fill="none" stroke="var(--orange)" stroke-width="1.3"/>
    <path d="M10,2.5 A4,4 0 0 1 13.5,6 M10,0.5 A6,6 0 0 1 15.5,6" fill="none" stroke="var(--orange)" stroke-width="1"/>
  </svg>
  <svg class="contact-icon" style="left:27px;top:391px" viewBox="0 0 16 16" aria-hidden="true">
    <g fill="none" stroke="var(--orange)" stroke-width="1.2">
      <circle cx="8" cy="8" r="6.5"/><ellipse cx="8" cy="8" rx="3" ry="6.5"/>
      <path d="M1.5,8 H14.5 M2.5,4.5 H13.5 M2.5,11.5 H13.5"/>
    </g>
  </svg>
  <ul class="office-lines">
    <li>48 Harlow RD, Brookfield Vale, Qld 4109 Australia</li>
    <li>1300 481 726</li>
    <li>+61 7 5550 3142</li>
    <li>www.quorin.com.au</li>
  </ul>

  <ul class="direct-lines">
    <li>XXXX XXX XXX</li>
    <li>declan@quorin.com.au</li>
  </ul>
  <svg class="contact-icon" style="left:625px;top:360px;width:24px;height:24px" viewBox="0 0 16 16" aria-hidden="true">
    <path d="M3,2 L5.5,2 L6.5,5 L5,6.3 C5.8,8 7.8,10 9.7,10.9 L11,9.4 L14,10.4 L14,13 C9,14 2,7 3,2 Z" fill="none" stroke="var(--orange)" stroke-width="1.1"/>
    <path d="M10,2.5 A4,4 0 0 1 13.5,6 M10,0.5 A6,6 0 0 1 15.5,6" fill="none" stroke="var(--orange)" stroke-width="0.9"/>
  </svg>
  <svg class="contact-icon" style="left:628px;top:395px;width:18px;height:14px" viewBox="0 0 18 14" aria-hidden="true">
    <rect x="1" y="1.5" width="16" height="11" fill="none" stroke="var(--orange)" stroke-width="1.3"/>
    <path d="M1,1.5 L9,8 L17,1.5" fill="none" stroke="var(--orange)" stroke-width="1.3"/>
  </svg>
</section>

<section class="card card-back" aria-label="Business card back">
  <div class="coverage-map" role="img" aria-label="Map of Australia and New Zealand showing Quorin distribution sites"></div>
  <span class="site-marker" style="left:510px;top:213px">QUORIN</span>
  <span class="site-marker" style="left:585px;top:248px">QUORIN</span>
  <span class="site-marker" style="left:495px;top:274px">QUORIN</span>
  <span class="site-marker" style="left:452px;top:299px">QUORIN</span>
  <span class="site-marker" style="left:251px;top:257px">QUORIN</span>

  <div class="claim-tag" style="top:10px">Distribution throughout AUS &amp; NZ</div>
  <div class="claim-tag" style="top:42px">HACCP Certified</div>
  <div class="claim-tag" style="top:71px">ISO 9001</div>

  <div class="range-group" style="top:24px">
    <h3 class="range-heading">Pallet Containment</h3>
    <ul class="range-list">
      <li>Stretch</li><li>Heat Shrink</li><li>Pallet Hood</li>
    </ul>
  </div>
  <div class="range-group" style="top:152px">
    <h3 class="range-heading">Flexible Packaging</h3>
    <ul class="range-list">
      <li>Bags &amp; Liners</li><li>Tube</li><li>Films &amp; Sheet</li><li>Printed films (12 col)</li><li>Shrink films</li>
    </ul>
  </div>
  <div class="range-group" style="top:340px">
    <h3 class="range-heading">Pallet Wrapping Machinery</h3>
    <ul class="range-list">
      <li>Semi &amp; Fully Auto Lines</li><li>Finance options&nbsp; include Lease, Rent, pay per wrap</li>
    </ul>
  </div>
</section>

</body>
</html>
```